Infographic for a Life Transformation brand to showcase their principle method

I need a clean infographic which would be used in a brochure to show the 5 steps to achieving a Inner Uprising. (ie Life transformation). I use the theme of a revolution so I would like the graphic to include a raised fist or something to represent a revolution and then the 5 points of information to represent each step.
Needs to very clean and simple. I don't want something that would take up a full page, I want it as a graphic, almost like a big logo. I don't want it laid out like a process chart.

My brand personalities from https://markcharacterhub.com.au/ are
The Everyman and The Magician to give you an idea of my brand.

I've attached my logo so that you can see the colour of it. Graphic doesn't need to match logo but should align with that colour.

Target Market(s)

Top Tier Executives, males, 35-55y old

Industry/Entity Type

Life Coaching

Requirements
Must have
• The graphic must have the 5 Steps: in this order
1.Clarity
2. Measurement
3. Discipline
4. Nutrition
5.Exercise
Nice to have
• It could include these action steps which line up with the 5 steps, It may be too much information by there is the option to include if it works.
1.see it
2. track it
3. do it
4. eat it
5. move it

```html
<!DOCTYPE html>
<html lang="en">
<head>
<meta charset="utf-8">
<title>Inner Uprising – Five Steps</title>
<link rel="stylesheet" href="https://fonts.googleapis.com/css2?family=Libre+Bodoni:wght@700&family=Montserrat:wght@800&family=Poppins:wght@500&family=Ubuntu:wght@500;700&display=swap">
<style>
  :root {
    --brand-blue: #0f4c92;
    --red: #e0232e;
    --red-dark: #9e1b22;
    --red-top: #f05a4a;
    --orange: #f7941d;
    --orange-dark: #e7601f;
    --orange-top: #fbb034;
    --teal: #2597a4;
    --teal-top: #4bc3c9;
    --blue-light: #42bde9;
    --blue-dark: #2e5a87;
    --green: #76bf43;
    --green-dark: #3d7a39;
    --green-top: #b3d453;
    --purple: #8b6db2;
    --purple-dark: #5e3e86;
    --purple-side: #673b8a;
    --purple-top: #a88fc2;
    --icon-grey: #58595b;
    --white: #ffffff;
  }
  html, body {
    margin: 0;
    padding: 0;
    width: 1200px;
    height: 849px;
    overflow: hidden;
    background: var(--white);
  }
  .infographic { display: block; width: 1200px; height: 849px; }
  .wordmark {
    font-family: "Poppins", sans-serif;
    font-weight: 500;
    font-size: 40px;
    letter-spacing: 9px;
    fill: var(--brand-blue);
  }
  .step-title {
    font-family: "Ubuntu", sans-serif;
    font-weight: 700;
    font-size: 42px;
    letter-spacing: 1px;
    fill: var(--white);
  }
  .step-copy {
    font-family: "Ubuntu", sans-serif;
    font-weight: 500;
    font-size: 24px;
    fill: var(--white);
  }
  .cube-number {
    font-family: "Libre Bodoni", serif;
    font-weight: 700;
    font-size: 120px;
    fill: var(--white);
  }
  .cube-action {
    font-family: "Montserrat", sans-serif;
    font-weight: 800;
    font-size: 40px;
    fill: var(--white);
  }
</style>
</head>
<body>
<svg class="infographic" viewBox="0 0 2268 1604" xmlns="http://www.w3.org/2000/svg">
  <defs>
    <linearGradient id="band-red" x1="0" x2="1"><stop offset="0" stop-color="var(--red)"/><stop offset="1" stop-color="var(--red-dark)"/></linearGradient>
    <linearGradient id="band-orange" x1="0" x2="1"><stop offset="0" stop-color="var(--orange)"/><stop offset="1" stop-color="var(--orange-dark)"/></linearGradient>
    <linearGradient id="band-blue" x1="0" x2="1"><stop offset="0" stop-color="var(--blue-light)"/><stop offset="1" stop-color="var(--blue-dark)"/></linearGradient>
    <linearGradient id="band-green" x1="0" x2="1"><stop offset="0" stop-color="var(--green)"/><stop offset="1" stop-color="var(--green-dark)"/></linearGradient>
    <linearGradient id="band-purple" x1="0" x2="1"><stop offset="0" stop-color="var(--purple)"/><stop offset="1" stop-color="var(--purple-dark)"/></linearGradient>
    <linearGradient id="row-shadow" x1="0" x2="1"><stop offset="0" stop-color="#000" stop-opacity="0"/><stop offset="0.3" stop-color="#000" stop-opacity="0.18"/><stop offset="1" stop-color="#000" stop-opacity="0.25"/></linearGradient>
    <radialGradient id="floor-shadow"><stop offset="0" stop-color="#000" stop-opacity="0.25"/><stop offset="1" stop-color="#000" stop-opacity="0"/></radialGradient>
  </defs>

  <!-- Brand wordmark -->
  <g class="brand">
    <rect x="580" y="280" width="60" height="60" fill="var(--brand-blue)"/>
    <text class="wordmark" x="610" y="443" text-anchor="middle">INNER UPRISING</text>
  </g>

  <!-- Step rows -->
  <g class="step-rows">
    <rect x="260" y="497" width="800" height="8" fill="url(#row-shadow)"/>
    <rect x="230" y="659" width="650" height="8" fill="url(#row-shadow)"/>
    <rect x="205" y="821" width="670" height="8" fill="url(#row-shadow)"/>
    <rect x="180" y="982" width="700" height="8" fill="url(#row-shadow)"/>
    <rect x="150" y="1144" width="730" height="8" fill="url(#row-shadow)"/>
    <rect x="120" y="1304" width="760" height="8" fill="url(#row-shadow)"/>

    <path class="band band-clarity" d="M440,503 H1040 V663 H545 C520,590 490,545 440,503 Z" fill="url(#band-red)"/>
    <path class="band band-measurement" d="M413,665 H880 V825 H518 C493,752 463,707 413,665 Z" fill="url(#band-orange)"/>
    <path class="band band-discipline" d="M386,827 H880 V986 H491 C466,913 436,869 386,827 Z" fill="url(#band-blue)"/>
    <path class="band band-nutrition" d="M359,988 H880 V1147 H464 C439,1074 409,1030 359,988 Z" fill="url(#band-green)"/>
    <path class="band band-exercise" d="M332,1150 H880 V1307 H437 C412,1234 382,1192 332,1150 Z" fill="url(#band-purple)"/>

    <g class="icon icon-clarity" fill="none" stroke="var(--icon-grey)" stroke-linecap="round">
      <circle cx="350" cy="573" r="38" stroke-width="12"/>
      <line x1="380" y1="603" x2="410" y2="633" stroke-width="20"/>
    </g>
    <circle class="icon icon-measurement" cx="342" cy="745" r="60" fill="#4fc0a8" role="img" aria-label="Pencil, pen and ruler icon"/>
    <circle class="icon icon-discipline" cx="330" cy="908" r="57" fill="#476b67" role="img" aria-label="Checklist clipboard icon"/>
    <circle class="icon icon-nutrition" cx="308" cy="1072" r="58" fill="#f0b92e" role="img" aria-label="Healthy food illustration"/>
    <circle class="icon icon-exercise" cx="282" cy="1228" r="57" fill="#e3efbf" role="img" aria-label="Running figure illustration"/>

    <text class="step-title" x="553" y="567">CLARITY</text>
    <text class="step-copy" x="553" y="607">Sequatib uscimporem qui</text>
    <text class="step-copy" x="553" y="637">as et odicipsam inctem</text>

    <text class="step-title" x="526" y="730">MEASUREMENT</text>
    <text class="step-copy" x="526" y="770">Sequatib uscimporem qui</text>
    <text class="step-copy" x="526" y="800">as et odicipsam inctem</text>

    <text class="step-title" x="499" y="889">DISCIPLINE</text>
    <text class="step-copy" x="499" y="929">Sequatib uscimporem qui</text>
    <text class="step-copy" x="499" y="959">as et odicipsam inctem</text>

    <text class="step-title" x="471" y="1047">NUTRITION</text>
    <text class="step-copy" x="471" y="1087">Sequatib uscimporem qui</text>
    <text class="step-copy" x="471" y="1117">as et odicipsam inctem</text>

    <text class="step-title" x="444" y="1210">EXERCISE</text>
    <text class="step-copy" x="444" y="1250">Sequatib uscimporem qui</text>
    <text class="step-copy" x="444" y="1280">as et odicipsam inctem</text>
  </g>

  <!-- Step cube -->
  <g class="step-cube">
    <ellipse cx="1220" cy="1400" rx="380" ry="50" fill="url(#floor-shadow)"/>

    <polygon class="layer-top" points="875,590 1258,380 1940,477 1555,685" fill="var(--purple-top)"/>
    <polygon class="layer-side" points="1555,685 1940,477 1940,1210 1555,1415" fill="var(--purple-side)"/>
    <polygon class="layer-front" points="875,590 1555,685 1555,1415 875,1322" fill="var(--purple)"/>

    <polygon class="layer-top" points="875,590 1190,418 1745,495 1430,668" fill="var(--green-top)"/>
    <polygon class="layer-front" points="875,590 1430,668 1430,1265 875,1190" fill="var(--green)"/>

    <polygon class="layer-top" points="875,590 1120,455 1555,515 1308,650" fill="var(--teal-top)"/>
    <polygon class="layer-front" points="875,590 1308,650 1308,1115 875,1058" fill="var(--teal)"/>

    <polygon class="layer-top" points="875,590 1050,493 1355,537 1183,632" fill="var(--orange-top)"/>
    <polygon class="layer-front" points="875,590 1183,632 1183,965 875,922" fill="var(--orange)"/>

    <polygon class="layer-top" points="875,590 985,530 1165,555 1060,615" fill="var(--red-top)"/>
    <polygon class="layer-front" points="875,590 1060,615 1060,815 875,790" fill="#ee3429"/>

    <text class="cube-number" x="962" y="765" text-anchor="middle">1</text>
    <text class="cube-action" transform="translate(1040 778) rotate(-90)">SEE IT</text>

    <text class="cube-number" x="1082" y="920" text-anchor="middle">2</text>
    <text class="cube-action" transform="translate(1160 930) rotate(-90)">TRACK IT</text>

    <text class="cube-number" x="1212" y="1060" text-anchor="middle">3</text>
    <text class="cube-action" transform="translate(1282 1073) rotate(-90)">DO IT</text>

    <text class="cube-number" x="1328" y="1212" text-anchor="middle">4</text>
    <text class="cube-action" transform="translate(1404 1223) rotate(-90)">EAT IT</text>

    <text class="cube-number" x="1453" y="1360" text-anchor="middle">5</text>
    <text class="cube-action" transform="translate(1528 1370) rotate(-90)">MOVE IT</text>
  </g>
</svg>
</body>
</html>
```